Halvorsen Partners Business Card

Halvorsen Partners Civil Construction
Marcus Halvorsen
CEO
727-518-6094
Marcus@HalvorsenSiteworks.example
www.HalvorsenSiteworks.example
Site Development
Utility Construction
Excavation
40876 County Lane 19
Land O' Lakes, FL 34638

Target Market(s)

Construction and government

Industry/Entity Type

Business

Contact Information for Business Card

I want an unique design that make a statement

Number of Pages Required

1 page

Font styles to use

Colors

Designer to choose colors to be used in the design.

Requirements
Must have
• unique design, feel free to modify or change the color of my logo.
Nice to have
• extra design features like spot UV, foil accents, color edges, unique paper, or any thing that would make my card pop.
• I like the feel of the image that I attached

```html
<!DOCTYPE html>
<html lang="en">
<head>
<meta charset="utf-8">
<title>Halvorsen Partners Business Card</title>
<link href="https://fonts.googleapis.com/css2?family=Jost:wght@400;500&family=Roboto:wght@400;500&family=Roboto+Condensed:wght@700&display=swap" rel="stylesheet">
<style>
  :root {
    --navy: #1f3f91;
    --navy-deep: #1b3884;
    --ink: #3a3d44;
    --grey: #6d7079;
    --rule: #8a8d94;
    --paper: #f3f3f2;
    --backdrop: #d9dadc;
    --white: #ffffff;
    --ghost: rgba(255, 255, 255, 0.09);
  }
  * { margin: 0; padding: 0; box-sizing: border-box; }
  html, body { width: 1200px; height: 799px; overflow: hidden; }
  body {
    background: var(--backdrop);
    position: relative;
    font-family: "Roboto", Arial, sans-serif;
  }
  .card {
    position: absolute;
    top: 50px;
    width: 400px;
    height: 700px;
    overflow: hidden;
  }
  .card--front { left: 170px; background: var(--paper); }
  .card--back { left: 630px; background: var(--navy); }

  /* front */
  .brand {
    position: absolute;
    top: 200px;
    left: 0;
    width: 100%;
    display: flex;
    align-items: center;
    justify-content: center;
    gap: 14px;
  }
  .brand__mark { width: 38px; height: 38px; background: var(--navy); flex: none; }
  .brand__words { font-family: "Jost", sans-serif; font-weight: 400; color: var(--navy); line-height: 1.15; }
  .brand__name { font-size: 21px; letter-spacing: 0.5px; text-transform: uppercase; }
  .brand__tag { font-size: 11px; letter-spacing: 4.2px; text-transform: uppercase; }

  .rule { position: absolute; left: 0; width: 100%; height: 1px; background: var(--rule); }
  .rule--upper { top: 352px; }
  .rule--lower { top: 520px; }

  .person { position: absolute; top: 392px; width: 100%; text-align: center; }
  .person__name {
    font-family: "Roboto Condensed", sans-serif;
    font-weight: 700;
    font-size: 25px;
    color: var(--navy);
    text-transform: uppercase;
    letter-spacing: 0.3px;
  }
  .person__role { font-size: 15px; color: var(--grey); margin-top: 4px; }

  .icons {
    position: absolute;
    top: 505px;
    left: 0;
    width: 100%;
    display: flex;
    justify-content: center;
    gap: 8px;
  }
  .icon { width: 30px; height: 30px; background: var(--navy); display: flex; align-items: center; justify-content: center; }
  .icon svg { width: 17px; height: 17px; }

  .contact { position: absolute; top: 556px; width: 100%; text-align: center; color: var(--ink); font-size: 15px; line-height: 1.5; }

  /* back */
  .back-brand { position: absolute; top: 96px; width: 100%; text-align: center; color: var(--white); }
  .back-brand__name { font-family: "Jost", sans-serif; font-weight: 500; font-size: 25px; letter-spacing: 0.5px; text-transform: uppercase; }
  .back-brand__tag { font-family: "Jost", sans-serif; font-size: 12px; letter-spacing: 5px; text-transform: uppercase; margin-top: 2px; }
  .services { position: absolute; top: 172px; width: 100%; list-style: none; text-align: center; color: var(--white); font-size: 15px; line-height: 1.45; }
  .services li::before {
    content: "";
    display: inline-block;
    width: 6px; height: 6px;
    background: var(--white);
    margin-right: 6px;
    vertical-align: middle;
    position: relative; top: -1px;
  }
  .back-block {
    position: absolute;
    left: 40px;
    top: 330px;
    width: 320px;
    height: 320px;
    background: var(--ghost);
  }
</style>
</head>
<body>
  <section class="card card--front">
    <div class="brand">
      <div class="brand__mark"></div>
      <div class="brand__words">
        <div class="brand__name">Halvorsen Partners</div>
        <div class="brand__tag">Civil Construction</div>
      </div>
    </div>

    <div class="rule rule--upper"></div>

    <div class="person">
      <div class="person__name">Marcus Halvorsen</div>
      <div class="person__role">CEO</div>
    </div>

    <div class="rule rule--lower"></div>
    <div class="icons">
      <div class="icon">
        <svg viewBox="0 0 24 24" aria-hidden="true"><path fill="#fff" d="M6.6 10.8a15.1 15.1 0 0 0 6.6 6.6l2.2-2.2a1 1 0 0 1 1-.25 11.4 11.4 0 0 0 3.6.57 1 1 0 0 1 1 1V20a1 1 0 0 1-1 1A17 17 0 0 1 3 4a1 1 0 0 1 1-1h3.5a1 1 0 0 1 1 1c0 1.25.2 2.45.57 3.57a1 1 0 0 1-.25 1z"/></svg>
      </div>
      <div class="icon">
        <svg viewBox="0 0 24 24" aria-hidden="true"><rect x="3" y="6" width="18" height="12" fill="#fff"/><path d="M3 6l9 7 9-7" fill="none" stroke="#1f3f91" stroke-width="1.6"/></svg>
      </div>
      <div class="icon">
        <svg viewBox="0 0 24 24" aria-hidden="true"><circle cx="12" cy="12" r="8.5" fill="none" stroke="#fff" stroke-width="1.8"/><ellipse cx="12" cy="12" rx="3.8" ry="8.5" fill="none" stroke="#fff" stroke-width="1.5"/><path d="M3.5 12h17" stroke="#fff" stroke-width="1.5"/></svg>
      </div>
    </div>

    <div class="contact">
      <div>727-518-6094</div>
      <div>Marcus@HalvorsenSiteworks.example</div>
      <div>www.HalvorsenSiteworks.example</div>
    </div>
  </section>

  <section class="card card--back">
    <div class="back-brand">
      <div class="back-brand__name">Halvorsen Partners</div>
      <div class="back-brand__tag">Civil Construction</div>
    </div>
    <ul class="services">
      <li>Site Development</li>
      <li>Utility Construction</li>
      <li>Excavation</li>
    </ul>
    <div class="back-block"></div>
  </section>
</body>
</html>
```